Modernise Business Card

Our company has been operating for 10 years. With the start of the new decade we are looking to refresh our business card design. We manufacture a range of industrial product shipping to customers internationally. A copy of our current card, both sides, is attached. We are looking for a mature professional appearance.

```html
<!DOCTYPE html>
<html lang="en">
<head>
<meta charset="utf-8">
<title>Veltrex Business Card</title>
<link rel="stylesheet" href="https://fonts.googleapis.com/css2?family=Poppins:wght@400;500;600;700&display=swap">
<style>
  :root {
    --stage: #eef0f0;
    --card-light: #e6e2e2;
    --brand-blue: #00a9d7;
    --back-blue: #00aad8;
    --ink: #1c1c1c;
    --icon-bg: #2a2a2a;
    --white: #ffffff;
  }
  * { margin: 0; padding: 0; box-sizing: border-box; }
  html, body {
    width: 1200px; height: 900px; overflow: hidden;
    background: var(--stage);
    font-family: "Poppins", sans-serif;
    color: var(--ink);
  }
  .sheet {
    width: 1200px; height: 900px;
    display: flex; flex-direction: column; align-items: center; justify-content: center;
    gap: 40px;
  }
  .card {
    width: 700px; height: 400px;
    position: relative;
    box-shadow: 0 6px 18px rgba(0,0,0,0.12);
  }
  /* Front */
  .card-front { background: var(--card-light); }
  .brand-name {
    position: absolute; top: 48px; right: 60px;
    font-size: 64px; font-weight: 700; line-height: 1;
    color: var(--brand-blue);
    letter-spacing: -1px;
  }
  .person {
    position: absolute; left: 60px; top: 150px;
  }
  .person-name {
    font-size: 32px; font-weight: 600; letter-spacing: 1.5px;
    text-transform: uppercase; line-height: 1.1;
  }
  .person-role {
    font-size: 18px; font-weight: 500; letter-spacing: 3.5px; line-height: 1.2;
  }
  .contact-list {
    position: absolute; left: 60px; top: 240px;
    list-style: none;
    display: flex; flex-direction: column; gap: 14px;
  }
  .contact-row { display: flex; align-items: center; gap: 18px; }
  .contact-icon {
    width: 40px; height: 40px; flex: none;
    background: var(--icon-bg);
    display: flex; align-items: center; justify-content: center;
  }
  .contact-text { font-size: 13.5px; font-weight: 500; line-height: 1.35; }
  /* Back */
  .card-back { background: var(--back-blue); }
  .back-content {
    position: absolute; left: 290px; top: 70px;
  }
  .back-brand {
    font-size: 68px; font-weight: 700; line-height: 1;
    color: var(--white); letter-spacing: -1px;
  }
  .product-list {
    list-style: none; margin-top: 40px;
    display: flex; flex-direction: column; gap: 12px;
  }
  .product-item {
    display: flex; align-items: center; gap: 12px;
    font-size: 18px; font-weight: 600;
  }
  .product-bullet {
    width: 14px; height: 14px; border: 2px solid var(--ink); border-radius: 50%;
    display: flex; align-items: center; justify-content: center;
  }
  .product-bullet::after {
    content: ""; width: 6px; height: 6px; background: var(--ink); border-radius: 50%;
  }
  .back-web {
    margin-top: 34px; font-size: 16px; font-weight: 500; letter-spacing: 1.5px;
  }
</style>
</head>
<body>
<main class="sheet">
  <section class="card card-front" aria-label="Card front">
    <div class="brand-name">Veltrex</div>
    <div class="person">
      <h1 class="person-name">Colin Marsh</h1>
      <p class="person-role">Your Designation</p>
    </div>
    <ul class="contact-list">
      <li class="contact-row">
        <span class="contact-icon">
          <svg width="22" height="22" viewBox="0 0 24 24" aria-hidden="true">
            <path d="M6.6 10.8a15 15 0 0 0 6.6 6.6l2.2-2.2a1 1 0 0 1 1-.25 11.4 11.4 0 0 0 3.6.57 1 1 0 0 1 1 1V20a1 1 0 0 1-1 1A17 17 0 0 1 3 4a1 1 0 0 1 1-1h3.5a1 1 0 0 1 1 1c0 1.25.2 2.45.57 3.57a1 1 0 0 1-.25 1z" fill="#fff"/>
          </svg>
        </span>
        <p class="contact-text">China : +86 155 2031 7748<br>Australia : +61 412 837 905</p>
      </li>
      <li class="contact-row">
        <span class="contact-icon">
          <svg width="22" height="22" viewBox="0 0 24 24" aria-hidden="true">
            <path d="M3 11 21 3l-6 18-3.5-7.5z" fill="none" stroke="#fff" stroke-width="1.6" stroke-linejoin="round"/>
            <path d="M11.5 13.5 21 3" stroke="#fff" stroke-width="1.6"/>
          </svg>
        </span>
        <p class="contact-text">Email : cmarsh@veltrexfittings.com<br>Web : www.veltrexfittings.com</p>
      </li>
      <li class="contact-row">
        <span class="contact-icon">
          <svg width="22" height="22" viewBox="0 0 24 24" aria-hidden="true">
            <path d="M12 2a7 7 0 0 0-7 7c0 5 7 13 7 13s7-8 7-13a7 7 0 0 0-7-7zm0 9.5A2.5 2.5 0 1 1 12 6.5a2.5 2.5 0 0 1 0 5z" fill="#fff"/>
          </svg>
        </span>
        <p class="contact-text">Address : Unit 8-3, Harbour View Tower 112 Lianfeng<br>Road Haishu District, Ningbo 315010 China</p>
      </li>
    </ul>
  </section>

  <section class="card card-back" aria-label="Card back">
    <div class="back-content">
      <div class="back-brand">Veltrex</div>
      <ul class="product-list">
        <li class="product-item"><span class="product-bullet"></span>Hydrolic Adapters</li>
        <li class="product-item"><span class="product-bullet"></span>House Fittings</li>
        <li class="product-item"><span class="product-bullet"></span>Quick Couplings</li>
      </ul>
      <p class="back-web">www.veltrexfittings.com</p>
    </div>
  </section>
</main>
</body>
</html>
```